"Tarvel Mouthguards " Custom-made Mouthguard Business Website

We need an informational website for our mouthguard Business "Tarvel Mouthguards". The logo is navy blue/lime green so want to have colour scheme that goes nicely with this - have uploaded our mouthguard flyer with some information we need to put into the website but I do have more information to put in there.

Target Market(s)

Sports clubs, sportspeople, parents and kids, schools

Industry/Entity Type

Dental, Custom-made Sports Mouthguards

Coding

Number of Pages Required

5+ page

Font styles to use
Serif
Sans Serif

Colors
0054AA
0677BA
7BADD7
CADEEF
E8F1F8
0094D4
00A9DD
6FCCEA
C7EBF8
E9F6FB
00AB8E
00BBA5
67D7C9
C6EFE9
E9F9F6
59FF00
82FF00
B8FF75
E3FFCB
F4FFEA
FFF300
FFF600
FEFA6F
FFFEC7
FFFEE8
FFC000
F8CF3A
FAE287
FDF2CF
FEFAEE
F0912C
F2A743
F7CA91
FBE8D2
FDF5EE
EE7325
F08F49
F5BC92
FAE3D3
FDF4ED

Requirements
Must have
• I want drop down pages, not one scrolling page. Different pages for each heading . Content uploaded - We need a general home page with lots of pictures and info that I'll provide. A page each dedicated to 1) About Us 2) Why choose a custom mouthguard? 3) Gallery 4) Contact Us. Will need logos from "Morvex"
Nice to have
• Mainly use greens and blues, but happy to pop in some yellow/oranges/red oranges if it looks good

```html
<!DOCTYPE html>
<html lang="en">
<head>
<meta charset="utf-8">
<title>Tarvel Mouthguards – Custom-Made Sports Mouthguards</title>
<link rel="stylesheet" href="https://fonts.googleapis.com/css2?family=Nunito:wght@400;600;700;800;900&family=Mulish:wght@400;500&display=swap">
<style>
:root{
  --navy:#0b2a6e;
  --navy-deep:#022a66;
  --purple:#3f1b9c;
  --purple-dark:#2c1178;
  --green:#35cc35;
  --blue:#1459c6;
  --icon-inner:#1f5bc4;
  --ink:#111111;
  --white:#ffffff;
}
*{margin:0;padding:0;box-sizing:border-box}
html,body{width:1200px;height:2560px;overflow:hidden}
body{position:relative;background:var(--white);font-family:"Nunito",sans-serif;color:var(--ink)}
.abs{position:absolute}

/* header */
.site-header{position:absolute;left:0;top:0;width:1200px;height:95px;background:var(--white)}
.brand{position:absolute;left:113px;top:16px;display:flex;align-items:center;gap:8px;color:var(--navy);font-weight:900;line-height:.95}
.brand-dot{width:14px;height:14px;border-radius:50%;background:var(--green)}
.brand-text{font-size:27px;letter-spacing:.5px}
.brand-text small{display:block;font-size:19px;letter-spacing:1px}
.main-nav{position:absolute;top:39px;left:0;font-size:14px;font-weight:800;color:var(--ink)}
.main-nav span{position:absolute;white-space:nowrap}
.main-nav .active{color:var(--green)}
.nav-underline{position:absolute;left:380px;top:62px;width:36px;height:3px;border-radius:2px;background:var(--green)}
.nav-cta{position:absolute;left:907px;top:28px;width:188px;height:40px;border:2px solid var(--purple);border-radius:5px;color:var(--purple);font-size:14px;font-weight:800;display:flex;align-items:center;justify-content:center}

/* hero */
.hero{position:absolute;left:0;top:95px;width:1200px;height:705px}
.hero-bg{position:absolute;inset:0;background:radial-gradient(ellipse at 60% 40%,#5a2db8 0%,var(--purple) 45%,var(--purple-dark) 100%)}
.hero-photo{position:absolute;left:300px;top:190px;width:640px;height:425px;border-radius:200px 200px 0 0;background:linear-gradient(180deg,rgba(250,210,70,.25),rgba(60,120,210,.35))}
.hero-title{position:absolute;left:0;width:1200px;text-align:center;color:var(--white)}
.hero-title h1{font-size:47px;font-weight:900;letter-spacing:.5px;margin-top:48px;line-height:54px}
.hero-title h2{font-size:31px;font-weight:800;line-height:36px}
.hero-title p{font-family:"Mulish",sans-serif;font-size:16px;margin-top:14px}
.btn{display:flex;align-items:center;justify-content:center;gap:12px;font-weight:800;font-size:18px;color:var(--white)}
.btn-ring{width:22px;height:22px;border-radius:50%;border:4px solid var(--white);position:relative}
.btn-ring::after{content:"";position:absolute;left:3px;top:3px;width:8px;height:8px;border-radius:50%;background:var(--white)}
.hero-btn{position:absolute;left:480px;top:189px;width:188px;height:52px;background:var(--green);border-radius:7px}
.hero-curves{position:absolute;left:0;top:0}

/* about */
.eyebrow{position:absolute;left:113px;top:863px;font-size:13px;color:var(--navy);font-weight:600}
.section-title{font-size:32px;font-weight:900;color:var(--navy);letter-spacing:.3px}
.about-title{position:absolute;left:113px;top:875px}
.rule-navy{position:absolute;height:5px;background:var(--navy)}
.rule-green{position:absolute;height:4px;background:var(--green)}
.about-text{position:absolute;left:112px;top:944px;width:458px;font-family:"Mulish",sans-serif;font-size:14px;line-height:25px;color:var(--ink)}
.read-more{position:absolute;left:113px;top:1120px;width:189px;height:51px;background:var(--navy-deep);border-radius:8px}
.product-backdrop{position:absolute;left:793px;top:808px;width:320px;height:320px;border-radius:50%;background:var(--navy-deep)}
.product-photo{position:absolute;left:630px;top:890px;width:540px;height:300px;border-radius:50%;background:radial-gradient(ellipse at 35% 55%,#4d4f5e,#8f90a0 55%,#ddd5e6 100%)}

/* why */
.why-title{position:absolute;left:0;top:1236px;width:1200px;text-align:center;color:var(--ink)}
.feature{position:absolute;top:1378px;width:190px;text-align:center}
.feature svg{display:block;margin:0 auto}
.feature p{width:160px;margin:52px auto 0;font-size:16px;line-height:20px;color:var(--ink);font-weight:600}
.gap-note{position:absolute;left:0;top:1643px;width:1200px;text-align:center;font-size:25px;font-weight:800;line-height:33px;color:var(--navy-deep)}

/* footer */
.footer-bg{position:absolute;left:0;top:1840px}
.footer-brand{position:absolute;left:113px;top:2140px;display:flex;align-items:center;gap:12px;color:var(--white);font-weight:900;line-height:.95}
.footer-brand .brand-text{font-size:52px}
.footer-brand .brand-text small{font-size:34px;letter-spacing:2px}
.footer-brand .brand-dot{width:22px;height:22px}
.footer-col{position:absolute;color:var(--white)}
.footer-col h3{font-size:19px;font-weight:700;margin-bottom:6px}
.sitemap{left:525px;top:2122px}
.sitemap li{list-style:none;font-family:"Mulish",sans-serif;font-size:15px;line-height:29px;display:flex;align-items:center;gap:5px}
.sitemap li::before{content:"";width:0;height:0;border-left:6px solid var(--white);border-top:4px solid transparent;border-bottom:4px solid transparent;margin-left:3px}
.location{left:770px;top:2123px;width:340px}
.contact-row{position:absolute;left:0;display:flex;gap:9px;font-family:"Mulish",sans-serif;font-size:15px;line-height:20px;white-space:nowrap}
.contact-row b{font-weight:700}
.contact-icon{width:30px;height:28px;border:1.5px solid var(--white);border-radius:4px;flex:none;display:flex;align-items:center;justify-content:center}
.copyright{position:absolute;left:113px;top:2400px;width:979px;height:88px;background:var(--white);border-radius:4px}
.copyright p{position:absolute;left:18px;top:33px;font-size:17px;color:var(--navy)}
.copyright p span{color:#1f9a1f;font-weight:600}
.partner{position:absolute;right:30px;top:28px;font-family:"Nunito",sans-serif;font-size:23px;font-weight:800;color:#1b9cd8;display:flex;align-items:center;gap:8px}
.partner i{width:14px;height:14px;border-radius:50%;background:#1b9cd8;display:block}
</style>
</head>
<body>

<header class="site-header">
  <div class="brand"><span class="brand-dot"></span><span class="brand-text">TARVEL<small>MOUTHGUARDS</small></span></div>
  <nav class="main-nav">
    <span class="active" style="left:377px">HOME</span>
    <span style="left:444px">ABOUT US</span>
    <span style="left:543px">OUR MOUTHGUARDS</span>
    <span style="left:717px">PHOTO GALLERY</span>
    <span style="left:864px">FAQ</span>
  </nav>
  <div class="nav-underline"></div>
  <div class="nav-cta">CONTACT / BOOKINGS</div>
</header>

<section class="hero">
  <div class="hero-bg" role="img" aria-label="Junior footballers training on a sports field under a purple colour wash"></div>
  <div class="hero-photo" role="img" aria-label="Two smiling kids in football jerseys holding a football and wearing coloured mouthguards"></div>
  <div class="hero-title">
    <h1>TARVEL MOUTHGUARDS</h1>
    <h2>Custom-Made Sports Mouthguards in Perth</h2>
    <p>Protect your smile with a comfortable, professional fit.</p>
  </div>
  <div class="hero-btn btn">Book Now <span class="btn-ring"></span></div>
  <svg class="hero-curves" width="1200" height="705" viewBox="0 95 1200 705">
    <path d="M0 635 Q600 800 1200 635 V800 H0 Z" fill="#ffffff"/>
    <path d="M0 635 Q600 800 1200 635" fill="none" stroke="#35cc35" stroke-width="6"/>
  </svg>
</section>

<div class="eyebrow">TARVEL MOUTHGUARDS</div>
<h2 class="section-title about-title">ABOUT ME</h2>
<div class="rule-navy" style="left:113px;top:918px;width:64px"></div>
<div class="rule-green" style="left:128px;top:927px;width:34px"></div>
<p class="about-text">Lorem Ipsum is simply dummy text of the printing and typesetting industry. Lorem Ipsum has been the industry's standard dummy text ever since the 1500s, when an unknown printer took a galley of type and scrambled it to make a type specimen book. It has survived not only five centuries, but also the leap into electronic typesetting, remaining essentially unchanged. It was popularised in.</p>
<div class="read-more btn">Read More <span class="btn-ring"></span></div>

<div class="product-backdrop"></div>
<div class="product-photo" role="img" aria-label="Custom mouthguards in speckled multicolour, black and white, and glitter finishes on round display discs"></div>

<h2 class="section-title why-title">WHY CHOOSE US</h2>
<div class="rule-navy" style="left:572px;top:1279px;width:64px"></div>
<div class="rule-green" style="left:588px;top:1288px;width:32px"></div>

<div class="feature" style="left:95px">
  <svg width="112" height="112" viewBox="0 0 112 112">
    <circle cx="56" cy="56" r="55" fill="#0b2a6e"/><circle cx="56" cy="56" r="34" fill="#1f5bc4"/>
    <circle cx="56" cy="43" r="5" fill="#fff"/><path d="M46 71 L52 53 H62 L66 61 L58 73 Z" fill="#fff"/>
    <path d="M52 63 L56 67 L63 58" fill="none" stroke="#1f5bc4" stroke-width="2.5"/>
  </svg>
  <p>Professionally made by a qualified dental prosthetist</p>
</div>
<div class="feature" style="left:286px">
  <svg width="112" height="112" viewBox="0 0 112 112">
    <circle cx="56" cy="56" r="55" fill="#0b2a6e"/><circle cx="56" cy="56" r="34" fill="#1f5bc4"/>
    <circle cx="56" cy="56" r="11" fill="none" stroke="#fff" stroke-width="3" stroke-dasharray="5 3"/><circle cx="56" cy="56" r="4" fill="#fff"/>
    <path d="M40 71 L50 61" stroke="#fff" stroke-width="3"/>
  </svg>
  <p>Custom fit for comfort, protection, and durability</p>
</div>
<div class="feature" style="left:494px">
  <svg width="112" height="112" viewBox="0 0 112 112">
    <circle cx="56" cy="56" r="55" fill="#0b2a6e"/><circle cx="56" cy="56" r="34" fill="#1f5bc4"/>
    <rect x="38" y="43" width="36" height="26" rx="4" fill="none" stroke="#fff" stroke-width="3"/><rect x="47" y="46" width="18" height="20" fill="#fff"/>
  </svg>
  <p>Wide range of colours and designs</p>
</div>
<div class="feature" style="left:710px">
  <svg width="112" height="112" viewBox="0 0 112 112">
    <circle cx="56" cy="56" r="55" fill="#0b2a6e"/><circle cx="56" cy="56" r="34" fill="#1f5bc4"/>
    <circle cx="56" cy="56" r="13" fill="none" stroke="#fff" stroke-width="3"/><path d="M50 56 L54 60 L62 51" fill="none" stroke="#fff" stroke-width="3"/>
    <circle cx="56" cy="56" r="20" fill="none" stroke="#fff" stroke-width="2" stroke-dasharray="2 5"/>
  </svg>
  <p>Available for kids, teens, and adults</p>
</div>
<div class="feature" style="left:920px">
  <svg width="112" height="112" viewBox="0 0 112 112">
    <circle cx="56" cy="56" r="55" fill="#0b2a6e"/><circle cx="56" cy="56" r="34" fill="#1f5bc4"/>
    <rect x="38" y="44" width="36" height="24" rx="2" fill="none" stroke="#fff" stroke-width="3"/><path d="M44 56 H60 M55 51 L60 56 L55 61" fill="none" stroke="#fff" stroke-width="3"/><path d="M56 44 V68" stroke="#fff" stroke-width="2"/>
  </svg>
  <p>Clinic and mobile school/club visits available</p>
</div>

<p class="gap-note">Talk to us about our “gap free” mouthguards for<br>eligible private health insurance members.</p>

<svg class="footer-bg" width="1200" height="720" viewBox="0 1840 1200 720">
  <path d="M0 1892 Q600 2120 1200 1892 V2560 H0 Z" fill="#1459c6"/>
  <path d="M0 1892 Q600 2120 1200 1892" fill="none" stroke="#35cc35" stroke-width="6"/>
</svg>

<footer>
  <div class="footer-brand"><span class="brand-dot"></span><span class="brand-text">TARVEL<small>MOUTHGUARDS</small></span></div>
  <div class="footer-col sitemap">
    <h3>Sitemap</h3>
    <ul>
      <li>Home</li><li>About Us</li><li>Our Mouthguards</li><li>Photo Gallery</li><li>FAQ</li><li>Contact / Bookings</li>
    </ul>
  </div>
  <div class="footer-col location">
    <h3>Location</h3>
    <div class="contact-row" style="top:34px">
      <span class="contact-icon"><svg width="14" height="18" viewBox="0 0 14 18"><path d="M7 17 C2 10 1 8 1 6 a6 6 0 0 1 12 0 c0 2-1 4-6 11Z" fill="none" stroke="#fff" stroke-width="1.5"/><circle cx="7" cy="6" r="2" fill="#fff"/></svg></span>
      <span><b>Address:</b><br>Unit 7, 14 Quarry Lane, Westfield,<br>Western Australia, 6100</span>
    </div>
    <div class="contact-row" style="top:110px;align-items:center">
      <span class="contact-icon"><svg width="16" height="16" viewBox="0 0 16 16"><path d="M3 1 L6 4 L4.5 6 C5.5 8.5 7.5 10.5 10 11.5 L12 10 L15 13 L13 15 C7 14 2 9 1 3 Z" fill="none" stroke="#fff" stroke-width="1.3"/></svg></span>
      <span><b>T:</b> 08 5550 2718</span>
    </div>
    <div class="contact-row" style="top:149px;align-items:center">
      <span class="contact-icon"><svg width="18" height="13" viewBox="0 0 18 13"><rect x="1" y="1" width="16" height="11" fill="none" stroke="#fff" stroke-width="1.3"/><path d="M1 1 L9 7 L17 1" fill="none" stroke="#fff" stroke-width="1.3"/></svg></span>
      <span><b>E:</b> hello@harbourdenturestudio.example</span>
    </div>
  </div>
  <div class="copyright">
    <p>Copyright © 2025 <span>Tarvel Mouthguards</span></p>
    <div class="partner"><i></i>Harbour Denture Studio</div>
  </div>
</footer>

</body>
</html>
```